Business Cards for a law firm

Business cards for our law firm. Use our silhoette logo and OAK HARBOR - check our website (www.oakharbor-legal.com)

Contact Information for Business Card

our silhouette logo, OAK HARBOR, 800-555-0147, Dorian Kestrup, dorian@oakharbor-legal.com

Requirements
Must have
• our silhouette logo, OAK HARBOR, 800-555-0147, Dorian Kestrup, dorian@oakharbor-legal.com

```html
<!DOCTYPE html>
<html lang="en">
<head>
<meta charset="utf-8">
<title>Oak Harbor Business Cards</title>
<link rel="stylesheet" href="https://fonts.googleapis.com/css2?family=Cinzel:wght@500;600;700&family=Montserrat:wght@300;400&display=swap">
<style>
  :root {
    --page: #ffffff;
    --card-white: #ffffff;
    --navy: #25346a;
    --navy-ink: #233266;
    --card-line: #e4e4e4;
    --white: #ffffff;
  }
  * { margin: 0; padding: 0; box-sizing: border-box; }
  html, body {
    width: 1200px;
    height: 1200px;
    overflow: hidden;
    background: var(--page);
  }
  .canvas {
    position: relative;
    width: 1200px;
    height: 1200px;
  }
  .card {
    position: absolute;
    left: 169px;
    width: 873px;
    height: 499px;
  }
  .card--front {
    top: 78px;
    background: var(--card-white);
    border: 1px solid var(--card-line);
  }
  .card--back {
    top: 630px;
    background: var(--navy);
  }
  .brand {
    position: absolute;
    left: 66px;
    top: 178px;
    display: flex;
    align-items: center;
    gap: 30px;
  }
  .brand__mark {
    width: 64px;
    height: 64px;
    background: var(--navy-ink);
  }
  .brand__name {
    font-family: "Cinzel", serif;
    font-weight: 700;
    font-size: 58px;
    letter-spacing: 6px;
    color: var(--navy-ink);
    line-height: 1;
  }
  .contact {
    position: absolute;
    left: 443px;
    top: 304px;
    color: var(--white);
  }
  .contact__name {
    font-family: "Cinzel", serif;
    font-weight: 600;
    font-size: 30px;
    letter-spacing: 3px;
    line-height: 1;
  }
  .contact__rule {
    width: 102px;
    height: 3px;
    background: var(--white);
    margin: 22px 0 24px 2px;
  }
  .contact__line {
    font-family: "Montserrat", sans-serif;
    font-weight: 400;
    font-size: 25px;
    line-height: 33px;
    letter-spacing: 0.3px;
  }
</style>
</head>
<body>
  <main class="canvas">
    <section class="card card--front" aria-label="Business card front">
      <div class="brand">
        <span class="brand__mark" aria-hidden="true"></span>
        <span class="brand__name">OAK HARBOR</span>
      </div>
    </section>

    <section class="card card--back" aria-label="Business card back">
      <div class="contact">
        <p class="contact__name">Dorian Kestrup</p>
        <div class="contact__rule"></div>
        <p class="contact__line">800-555-0147</p>
        <p class="contact__line">dorian@oakharbor-legal.com</p>
      </div>
    </section>
  </main>
</body>
</html>
```